Mortgage Broking boutique Business

I’m wanting a revamped look to my existing business card design. I do like the black and silver but happy to have other colours introduced based on your creation. I’ve attached a copy of my current card so you can have a starting point updated details noted brloe. I deal with high net worth individuals so need my card to be sophisticated, classy that gives off a classy vibe

Target Market(s)

High net worth, wealthy

Industry/Entity Type

Mortgage Brokerage

Contact Information for Business Card

Job title: Finance Executive
Phone: +61 7 3287 4419
Mobile: 0471 352 608
Email: marcus@quillbrookcapital.com.au
Web: www.quillbrookcapital.com.au
Address: level 36 Tindale Court, 58 Harwick St Brisbane QLD 4000

Font styles to use
Other font styles liked:
• Helvetica

Colors

Designer to choose colors to be used in the design.

Requirements
Must have
• Use my existing card design as a starting point

```html
<!DOCTYPE html>
<html lang="en">
<head>
<meta charset="utf-8">
<title>Quillbrook Capital – Business Card</title>
<link href="https://fonts.googleapis.com/css2?family=Arimo:wght@400;700&display=swap" rel="stylesheet">
<style>
  :root{
    --backdrop:#2c2c2e;
    --card:#0b0b0b;
    --ink-white:#f2f2f2;
    --ink-grey:#9a9a9a;
    --rule:#6e6e6e;
    --flourish-grey:#3e3e3e;
    --gold-light:#f4e6a6;
    --gold:#d8b44a;
    --gold-deep:#a88420;
    --silver-1:#8f8f92;
    --silver-2:#e4e4e6;
    --silver-3:#bdbdc0;
  }
  *{box-sizing:border-box;margin:0;padding:0}
  html,body{width:1200px;height:674px;overflow:hidden}
  body{background:var(--backdrop);font-family:"Arimo",Helvetica,Arial,sans-serif;position:relative}

  .card{position:absolute;background:var(--card);box-shadow:0 14px 30px rgba(0,0,0,.45);overflow:hidden}

  /* Front */
  .card--front{left:110px;top:340px;width:460px;height:280px}
  .front__flourish{position:absolute;left:90px;width:280px;height:30px;border-radius:15px;
    background:linear-gradient(90deg,#6f6552,#b9ad8c 50%,#6f6552)}
  .front__flourish--top{top:48px}
  .front__flourish--bottom{top:202px}
  .front__band{position:absolute;left:0;right:0;top:86px;height:108px;
    background:linear-gradient(90deg,var(--silver-1) 0%,var(--silver-2) 18%,var(--silver-3) 35%,var(--silver-2) 55%,var(--silver-3) 75%,var(--silver-1) 100%);
    border-top:3px solid var(--gold);border-bottom:3px solid var(--gold);
    display:flex;flex-direction:column;align-items:center;justify-content:center;gap:4px}
  .front__name{color:#1a1a1a;font-size:22px;font-weight:400;letter-spacing:6px;line-height:1.15}

  /* Back */
  .card--back{left:610px;top:50px;width:540px;height:320px}
  .back__logo{position:absolute;left:30px;top:26px}
  .back__logo-line{display:block;color:var(--ink-grey);font-size:20px;font-weight:400;letter-spacing:6px;line-height:1.2}

  .rule{position:absolute;height:2px;background:var(--rule)}
  .rule::before,.rule::after{content:"";position:absolute;top:-2px;width:6px;height:6px;border-radius:50%;background:var(--rule)}
  .rule::before{left:-3px}.rule::after{right:-3px}
  .rule--top{left:30px;top:92px;width:240px}
  .rule--right{left:360px;top:172px;width:150px}
  .rule--bottom-left{left:30px;top:292px;width:200px}
  .rule--bottom-right{left:310px;top:292px;width:200px}

  .back__flourish{position:absolute;width:60px;height:22px;border-radius:11px;background:var(--flourish-grey)}
  .back__flourish--top{left:282px;top:82px}
  .back__flourish--bottom{left:240px;top:282px}

  .back__person{position:absolute;right:30px;top:104px;text-align:right}
  .back__person-name{color:var(--ink-white);font-size:26px;font-weight:400;letter-spacing:1px}
  .back__person-role{color:var(--ink-white);font-size:22px;font-weight:700;margin-top:4px}

  .contact{position:absolute;display:flex;align-items:center;gap:10px;color:var(--ink-white);font-size:14px;line-height:24px}
  .contact__icon{width:24px;height:24px;border-radius:50%;flex:none;
    background:radial-gradient(circle at 35% 30%,var(--gold-light),var(--gold) 55%,var(--gold-deep));
    display:flex;align-items:center;justify-content:center}
  .contact__icon svg{width:13px;height:13px}
  .contact--phone{left:30px;top:112px}
  .contact--mobile{left:30px;top:148px}
  .contact--email{left:270px;top:188px}
  .contact--web{left:270px;top:220px}
  .contact--address{left:30px;top:256px;font-size:13.5px}
</style>
</head>
<body>

<section class="card card--front" aria-label="Card front">
  <div class="front__flourish front__flourish--top" role="img" aria-label="Gold scroll flourish above the band"></div>
  <div class="front__band">
    <span class="front__name">QUILLBROOK</span>
    <span class="front__name">CAPITAL</span>
  </div>
  <div class="front__flourish front__flourish--bottom" role="img" aria-label="Gold scroll flourish below the band"></div>
</section>

<section class="card card--back" aria-label="Card back">
  <div class="back__logo">
    <span class="back__logo-line">QUILLBROOK</span>
    <span class="back__logo-line">CAPITAL</span>
  </div>
  <div class="rule rule--top"></div>
  <div class="back__flourish back__flourish--top" role="img" aria-label="Grey scroll flourish at the end of the rule"></div>

  <div class="back__person">
    <div class="back__person-name">MARCUS WREN</div>
    <div class="back__person-role">Finance Executive</div>
  </div>
  <div class="rule rule--right"></div>

  <div class="contact contact--phone">
    <span class="contact__icon"><svg viewBox="0 0 16 16"><path d="M4 1.5l2.2 2.6-1.3 1.6c.9 2 2.4 3.5 4.4 4.4l1.6-1.3 2.6 2.2-1.3 2.2C7 13 3 9 1.8 2.8z" fill="#1a1a1a"/></svg></span>
    <span>+61 7 3287 4419</span>
  </div>
  <div class="contact contact--mobile">
    <span class="contact__icon"><svg viewBox="0 0 16 16"><rect x="4.5" y="1.5" width="7" height="13" rx="1.2" fill="none" stroke="#1a1a1a" stroke-width="1.5"/><circle cx="8" cy="12" r=".9" fill="#1a1a1a"/></svg></span>
    <span>0471 352 608</span>
  </div>
  <div class="contact contact--email">
    <span class="contact__icon"><svg viewBox="0 0 16 16"><rect x="2" y="4" width="12" height="8.5" fill="none" stroke="#1a1a1a" stroke-width="1.4"/><path d="M2 4l6 5 6-5" fill="none" stroke="#1a1a1a" stroke-width="1.4"/></svg></span>
    <span>marcus@quillbrookcapital.com.au</span>
  </div>
  <div class="contact contact--web">
    <span class="contact__icon"><svg viewBox="0 0 16 16"><circle cx="8" cy="8" r="6" fill="none" stroke="#1a1a1a" stroke-width="1.3"/><ellipse cx="8" cy="8" rx="2.6" ry="6" fill="none" stroke="#1a1a1a" stroke-width="1.1"/><path d="M2 8h12" stroke="#1a1a1a" stroke-width="1.1"/></svg></span>
    <span>www.quillbrookcapital.com.au</span>
  </div>
  <div class="contact contact--address">
    <span class="contact__icon"><svg viewBox="0 0 16 16"><path d="M8 1.5a4.5 4.5 0 0 1 4.5 4.5c0 3.3-4.5 8.5-4.5 8.5S3.5 9.3 3.5 6A4.5 4.5 0 0 1 8 1.5z" fill="#1a1a1a"/><circle cx="8" cy="6" r="1.6" fill="#d8b44a"/></svg></span>
    <span>Level 36 Tindale Court, 58 Harwick St Brisbane QLD 4000</span>
  </div>

  <div class="rule rule--bottom-left"></div>
  <div class="back__flourish back__flourish--bottom" role="img" aria-label="Grey scroll flourish between the lower rules"></div>
  <div class="rule rule--bottom-right"></div>
</section>

</body>
</html>
```